www.brevatin.com Sales/Order Page ReDesign

We need a new and amazing design for our sales/order page to attract more costumers and new houses for our portal.

Here is the existing page with the current design: https://www.brevatin.com/sales

We are proud owners of www.sommarhytta.no and www.brevatin.com and we want more holiday home owners to join our page so that we can rent out their holiday homes and increase the number of houses on our portal.

To get more homeowners we need a sales page that can sell our products the best way possible. Therefore we want you too blow us away with a fresh, modern, easy understandable and stylish new sales/order page.

The only restrictions we give when it comes to design is that it needs to fit the existing design of our portals, the top and footer are set. Beside that we are open for everything as long as it at once give the customers impression that this is a good, professional page were they just have to put out their houses.

When it comes to content I have added two documents who include the content to put in here and some guidelines on how to organize the page. Please be creative and add necessary graphics, symbols, background pictures and what ever necessary to make this page look professional and appealing to new costumers.

Looking forward to what suggestions we are given.

We just want to inform that we have updated our brief with a much more concrete description of what content to add on the sale page, and who to structure the content on the page. Hope this helps to make suggestions easier. Looking forward to receive some good contributions.

We would just like to make sure that everyone have understood that we are not asking for a new design suggestion to our portal in general. We are only asking for a redesign of our sales/order page you find here www.brevatin.com/sales. We have to day received some designs for our front page and the design it self was good, but that's not what we are asking for this time and don't want you to use time of something we don't need at the moment. We are looking forward too se some good suggestions.

Reason: Hello. Thanks for all the great contributions we have been given so fare. We haven't been able to respond to all design and are therefore extending the deadline so that we are able to respond to the designs we have been giver and to gov time to make final changes.

Reason: We are extending the deadline to give designers time to give new suggestion based on our latest feedback today.

Reason: Extended so we can receive last design changes.

Target Market(s)

This is a presentation page where we present our product agains new home owner who we what to choose listing there property on or site.

Industry/Entity Type

Sales

Requirements
Must have
• A modern design who calms the costumer down and help them in deciding to chose us, and for them to choose us they need to trust and believe in us. Therefore your main task is to create a page that effectively informs about our product, gets the visitors attentions and make them trust us.
Nice to have
• Examples of good competitors and good order pages we like:

http://www.cabinquest.example/info/lyp?icid=IL___O_Text___top_nav_link
https://www.nestlodge.example/rooms/new
https://www.pearvix.example/phone/compare/
http://www.guestnook.example/host
Should not have
• - Bad design :-). With bad design we mean design that looks like it's made in 2 seconds by a little child.

```html
<!DOCTYPE html>
<html lang="en">
<head>
<meta charset="utf-8">
<title>Sales &amp; Order</title>
<link rel="stylesheet" href="https://fonts.googleapis.com/css2?family=Raleway:wght@400;500;600&display=swap">
<style>
:root{
  --blue:#0a88d0;
  --blue-light:#aaeefc;
  --green:#88d000;
  --green-line:#88c521;
  --green-soft:#f2f9e6;
  --orange:#ff6d00;
  --orange-soft:#fdf1ec;
  --ink:#111;
  --muted:#a9a9a9;
  --panel:#fafafa;
  --header-bg:#f3f3f3;
  --white:#fff;
}
*{box-sizing:border-box;margin:0;padding:0}
html,body{width:1200px;height:836px;overflow:hidden;background:var(--white);font-family:"Raleway",sans-serif;color:var(--ink)}
.page{position:relative;width:1200px;height:836px}
.plans{position:absolute;left:100px;top:0;width:1000px;height:328px;border-bottom:3px solid var(--green-line)}
.plan{position:absolute;top:0;height:325px}
.plan--basic{left:0;width:334px}
.plan--plus{left:334px;width:330px;border-left:1px solid var(--blue)}
.plan--pro{left:664px;width:336px;border-left:1px solid var(--blue);background:#f9fcfe}
.site{position:absolute;width:152px;height:46px;border:1px solid #ddd;background:var(--white);display:flex;align-items:center;justify-content:center;font-size:14px;font-weight:600;color:var(--blue)}
.site--a{top:-16px}
.site--b{top:34px}
.site--c{top:84px;border-color:#333}
.plan--basic .site{left:59px}
.plan--plus .site,.plan--pro .site{left:54px}
.upgrade{position:absolute;left:35px;top:96px;font-size:14.5px;display:flex;align-items:center;gap:9px}
.upgrade .dot{width:11px;height:11px;border-radius:50%;background:#e6e6e6}
.prices{position:absolute;left:56px;top:123px;font-size:12px;line-height:15px;border-collapse:collapse}
.prices td{padding:0}
.prices .n{width:22px}
.prices .u{width:86px;color:var(--muted)}
.prices .u--year{padding-left:2px}
.btn{position:absolute;height:50px;border-radius:25px;display:flex;align-items:center;justify-content:center;color:var(--white);font-size:19px}
.btn--choose{top:253px;width:260px;background:var(--blue)}
.plan--basic .btn{left:40px}
.plan--plus .btn{left:36px}
.plan--pro .btn{left:35px;background:var(--blue-light);color:#1a2a33}
.actions{position:absolute;left:100px;top:328px;width:1000px;height:508px;background:var(--panel)}
.card{position:absolute;top:17px;height:200px;width:480px;padding:25px 22px 0;font-size:14px;line-height:24px}
.card--add{left:20px;background:var(--green-soft);padding-right:40px}
.card--contact{left:500px;background:var(--orange-soft);padding-left:12px;padding-right:36px}
.card .btn{top:100px;width:450px;font-size:14.5px;font-weight:500}
.card--add .btn{left:21px;background:var(--green)}
.card--contact .btn{left:11px;background:var(--orange)}
.hint{position:absolute;left:0;top:242px;width:1000px;height:48px;background:var(--green-soft);padding:15px 35px;font-size:12px;white-space:nowrap}
.hint a{color:var(--blue)}
.section-head{position:absolute;left:0;top:290px;width:1000px;height:72px;background:var(--header-bg);padding:22px 35px;font-size:24px;font-weight:500}
.field-label{position:absolute;left:40px;font-size:14.5px}
.field{position:absolute;width:252px;height:52px;border:1px solid var(--blue);background:var(--white);padding:0 31px;display:flex;align-items:center;font-size:14.5px}
.field--select{justify-content:space-between;padding-right:18px}
.field--select svg{width:11px;height:9px}
.field .ph{color:var(--muted)}
</style>
</head>
<body>
<div class="page">
  <section class="plans">
    <div class="plan plan--basic">
      <div class="site site--a">Fjordlys.no</div>
      <div class="site site--b">Havnly</div>
      <div class="site site--c">Vidda</div>
      <div class="btn btn--choose">Choose This</div>
    </div>
    <div class="plan plan--plus">
      <div class="site site--a">Fjordlys.no</div>
      <div class="site site--b">Havnly</div>
      <div class="upgrade"><span class="dot"></span>Upgrade Option for Vidda</div>
      <table class="prices">
        <tr><td class="n">60</td><td class="u">days</td><td>€ &nbsp;&nbsp;50</td></tr>
        <tr><td class="n">120</td><td class="u">days</td><td>€ &nbsp;&nbsp;90</td></tr>
        <tr><td class="n">240</td><td class="u">days</td><td>€ 160</td></tr>
        <tr><td class="n">1</td><td class="u u--year">year</td><td>€ 240</td></tr>
      </table>
      <div class="btn btn--choose">Choose This</div>
    </div>
    <div class="plan plan--pro">
      <div class="site site--a">Fjordlys.no</div>
      <div class="site site--b">Havnly</div>
      <div class="upgrade"><span class="dot"></span>Upgrade Option for Vidda</div>
      <table class="prices">
        <tr><td class="n">60</td><td class="u">days</td><td>€ &nbsp;&nbsp;50</td></tr>
        <tr><td class="n">120</td><td class="u">days</td><td>€ &nbsp;&nbsp;90</td></tr>
        <tr><td class="n">240</td><td class="u">days</td><td>€ 160</td></tr>
        <tr><td class="n">1</td><td class="u u--year">year</td><td>€ 240</td></tr>
      </table>
      <div class="btn btn--choose">Choose This</div>
    </div>
  </section>

  <section class="actions">
    <div class="card card--add">
      You have not chosen to list any property with us, add a property by clicking Add New Property below
      <div class="btn">Add New Property</div>
    </div>
    <div class="card card--contact">
      If you want us to contact you too answer any question Contact Us button
      <div class="btn">Contact Us</div>
    </div>
    <p class="hint">You now know that you are going to list your property, but are uncertain which listing option is right for you? <a href="#">Click here</a> to calculate what's most profitable for you..</p>
    <h2 class="section-head">Customer Detail</h2>
    <span class="field-label" style="top:433px">Customer Type</span>
    <div class="field field--select" style="left:288px;top:418px">Private Customer
      <svg viewBox="0 0 11 9"><path d="M0 0h11L5.5 9z" fill="#0a88d0"/></svg>
    </div>
    <span class="field-label" style="top:493px">Customer Name</span>
    <div class="field" style="left:288px;top:478px"><span class="ph">First Name</span></div>
    <div class="field" style="left:558px;top:478px"><span class="ph">Last Name</span></div>
  </section>
</div>
</body>
</html>
```